Thoroughbred Racing Partnership needs web design

Crest of Fortune Partners is a management group who buys horses and races them on both the West and East coasts. The premise of the business is for an investment as little as $500, anyone can be a partner and own a percentage of a horse(s). This is a low cost way of getting involved in the exciting sport of Thoroughbred Racing, without shouldering the heavy financial responsibility. Our target market is mostly males 40+ but we want to include all target markets. We are looking for something very clean and professional, we want to give an image of success. Nothing overly "artsy." I have included the logo in which you can incorporate in the site. Also, the logo colors will be the colors of our "silks." The silks are what the jockey wears and will be an important marketing tool for COF. We would like a very prominent picture of a racehorse somewhere on the homepage, we want to make it clear that is a website for Horseracing partnerships.

On the top of the site, it should say "Crest of Fortune" (on the top)
and below that "Thoroughbred Racing Partnerships." (below that)

The main sections, which should be across the top are:

Home
About Us
Ownership
Stable Roster
News
Contact us

Some of these will have drop down menus.

An example of a competitor website that we like is: www.harlowfieldeq.example
An example of a competitor website that we don't like is: www.gallopvane.example
Updates

Project Deadline Extended
Reason: We have a Board of Directors meeting on the 22nd and we will be making a decision on that day. I'm giving an extension so that all designers are able to submit their designs by the 22nd. Thank you!

Target Market(s)

40+ males

Industry/Entity Type

Business

Requirements
Must have
• our logo must be on the site. We would like at least one bold image of a thoroughbred horse in action. The picture is going to tell the story so it needs to be very eye-catching.

Our slogan should also be included on the website, "Experience the thrill of owning a Racehorse."
Should not have
• cartoons, artsy pictures, pictures of Steeplechase horses or "jumpers." This partnership is for racehorses only, there is not jumping involved with the horses.

```html
<!DOCTYPE html>
<html lang="en">
<head>
<meta charset="utf-8">
<title>Crest of Fortune Partners</title>
<link href="https://fonts.googleapis.com/css2?family=Kumbh+Sans:wght@400;600;700&family=Arimo:wght@400&display=swap" rel="stylesheet">
<style>
:root{
  --red:#a8232f;
  --red-dark:#9b1b2b;
  --red-soft:#d9868c;
  --white:#ffffff;
  --ink:#333333;
  --footer:#d9d9d9;
  --footer-grey:#a3a3a3;
  --black:#111111;
}
*{margin:0;padding:0;box-sizing:border-box}
html,body{width:1200px;height:951px;overflow:hidden;background:var(--white)}
body{position:relative;font-family:"Arimo",Arial,sans-serif;color:var(--ink)}
.display{font-family:"Kumbh Sans",Helvetica,sans-serif}

.hero-photo{position:absolute;left:0;top:75px;width:1200px;height:441px;
  background:linear-gradient(100deg,#4a3424 0%,#7a4a2c 28%,#9aa59a 48%,#8cc4e6 62%,#a9d3ee 80%,#cfe6f5 100%)}
.header-shape{position:absolute;left:0;top:0;width:1200px;height:145px}

.brand-name{position:absolute;text-align:center;font-family:"Kumbh Sans",sans-serif;
  font-weight:700;font-size:24px;line-height:28px}
.brand-name.header{left:150px;top:44px;width:216px;color:var(--red)}
.brand-name.footer-mark{left:870px;top:58px;width:212px;color:var(--footer-grey)}

.social{position:absolute;left:657px;top:24px;display:flex;gap:5px}
.social span{width:32px;height:32px;border-radius:50%;background:var(--red-soft);display:block}
.divider{position:absolute;left:828px;top:9px;width:1px;height:57px;background:#c04a54}
.phone{position:absolute;left:855px;top:26px;display:flex;align-items:center;gap:10px;
  color:var(--red-soft);font-size:25px;font-weight:700}

.nav{position:absolute;top:95px;left:0;width:1200px;font-family:"Kumbh Sans",sans-serif;
  font-size:13px;font-weight:700;color:var(--white);letter-spacing:.2px}
.nav a{position:absolute;color:inherit;text-decoration:none;white-space:nowrap}
.nav .drop::after{content:"";display:inline-block;margin-left:10px;border:5px solid transparent;border-top:6px solid var(--white);vertical-align:-2px}

.hero-title{position:absolute;left:724px;top:220px;color:var(--red);font-size:45px;font-weight:700;letter-spacing:-.5px}
.hero-sub{position:absolute;left:731px;top:272px;color:var(--white);font-size:20px;font-weight:600}
.hero-btn{position:absolute;left:729px;top:317px;width:325px;height:70px;border-radius:8px;
  background:linear-gradient(#5a5a5a,#1c1c1c 55%,#000);color:var(--white);font-size:20px;font-weight:700;
  display:flex;align-items:center;padding-left:25px;gap:20px}

.feature-card{position:absolute;left:742px;top:471px;width:366px;height:250px;background:var(--white);
  border-radius:4px;box-shadow:0 10px 22px rgba(0,0,0,.18);padding:10px}
.feature-card .photo{width:100%;height:230px;background:linear-gradient(180deg,#5b4330 0%,#6b4a32 45%,#7e9a55 70%,#6f9c45 100%)}

.intro{position:absolute;left:125px;top:555px;width:580px}
.intro h1{color:var(--red-dark);font-size:28px;font-weight:700;letter-spacing:-.4px}
.intro p{margin-top:14px;font-size:12.2px;line-height:20.5px;color:var(--ink)}
.intro .more{position:absolute;left:463px;top:120px;color:var(--red-dark);font-size:16px;font-weight:700;text-decoration:underline}

.footer{position:absolute;left:0;top:771px;width:1200px;height:180px;background:var(--footer);border-bottom:3px solid var(--black)}
.footer h2{position:absolute;font-size:21px;font-weight:600;color:var(--footer-grey)}
.sitemap{position:absolute;left:128px;top:94px;display:grid;grid-template-columns:105px 103px 80px;row-gap:6px;font-size:12.5px;color:var(--black)}
.address{position:absolute;right:362px;top:96px;text-align:right;font-size:12.5px;line-height:19px;color:var(--black)}
</style>
</head>
<body>

<div class="hero-photo" role="img" aria-label="Photograph of thoroughbred racehorses with jockeys galloping past a tote board"></div>

<svg class="header-shape" viewBox="0 0 1200 145" aria-hidden="true">
  <rect x="0" y="7" width="1200" height="68" fill="#a8232f"/>
  <path d="M40 7 Q80 7 110 45 L135 95 Q165 137 215 137 L355 137 Q395 137 420 105 L455 55 Q490 7 540 7 Z" fill="#fff"/>
  <path d="M460 75 L475 75 L463 85 Z" fill="#a8232f"/>
</svg>

<div class="brand-name header">Crest of Fortune<br>Partners</div>

<div class="social" aria-label="Social links"><span></span><span></span><span></span><span></span></div>
<div class="divider"></div>
<div class="phone display">
  <svg width="26" height="26" viewBox="0 0 24 24" aria-hidden="true"><path d="M6.6 10.8a15 15 0 0 0 6.6 6.6l2.2-2.2a1 1 0 0 1 1-.25 11.4 11.4 0 0 0 3.6.57 1 1 0 0 1 1 1V20a1 1 0 0 1-1 1A17 17 0 0 1 3 4a1 1 0 0 1 1-1h3.5a1 1 0 0 1 1 1c0 1.25.2 2.45.57 3.6a1 1 0 0 1-.25 1z" fill="none" stroke="#d9868c" stroke-width="1.6"/></svg>
  1800-4417 2093
</div>

<nav class="nav">
  <a style="left:441px">HOME</a>
  <a class="drop" style="left:530px">ABOUT US</a>
  <a style="left:638px">OWNERSHIP</a>
  <a class="drop" style="left:749px">STABLE ROSTER</a>
  <a style="left:909px">NEWS</a>
  <a style="left:995px">CONTACT US</a>
</nav>

<div class="hero-title display">Crest of Fortune</div>
<div class="hero-sub display">Thoroughbred Racing Partnerships.</div>
<a class="hero-btn display">Learn About Partnerships
  <svg width="18" height="26" viewBox="0 0 18 26" aria-hidden="true"><path d="M3 3 L13 13 L3 23" fill="none" stroke="#fff" stroke-width="4"/></svg>
</a>

<div class="feature-card"><div class="photo" role="img" aria-label="Photograph of racehorses galloping on a turf course"></div></div>

<section class="intro">
  <h1 class="display">Experience the thrill of owning a Racehorse.</h1>
  <p>Lorem ipsum dolor sit amet, consectetur adipiscing elit. Donec eleifend diam id vulputate dictum. Morbi sagittis dui sit amet ultricies pharetra. Vestibulum sagittis turpis a fermentum interdum. Mauris sapien arcu, sollicitudin at diam eget, posuere lobortis turpis. Morbi nisi odio, congue eu leo a, sollicitudin congue leo.</p>
  <a class="more display">READ MORE</a>
</section>

<footer class="footer">
  <h2 class="display" style="left:128px;top:61px">Sitemap</h2>
  <div class="sitemap">
    <span>Home</span><span>Stable Roster</span><span>Ownership</span>
    <span>About Us</span><span>News</span><span>Contact us</span>
  </div>
  <h2 class="display" style="right:368px;top:63px">COF Partners</h2>
  <div class="address">Lorem ipsum Street it amet, consectetur adipiscing elit. Donec<br>P: 1800 - 4417 2093, E: email@cofpartners.example</div>
  <div class="brand-name footer-mark">Crest of Fortune<br>Partners</div>
</footer>

</body>
</html>
```